existing Business Card Re design

We are wanting to re design our cards to reflect our new logo , i have attache the current business cards and new logo
i will need a business card that reflects the following information on each card.

card 1:
Gordon Thibeaux, President
555-182-4407
info@qlmcoatingpro.example

card 2:
Lionel Ostrander, Outside Sales
Office: 555-182-4407
Cell: 555-631-2958
Sales@qlmcoatingpro.example

Card 3
Tomas Varley, Branch Manager
Office: 555-182-4407
Cell: 555-274-8163
Tomas@qlmcoatingpro.example

Card 4
I will need a Generic card with no name on it just business
555-182-4407
info@qlmcoatingpro.example

Target Market(s)

Homeowners and Contractors

Contact Information for Business Card

We are wanting to re design our cards to reflect our new logo , i have attache the current business cards and new logo. same info on current card

card 1:
Gordon Thibeaux, President
555-182-4407
info@qlmcoatingpro.example

card 2:
Office: 555-182-4407
Cell: 555-631-2958
Sales@qlmcoatingpro.example

Card 3
Office: 555-182-4407
Cell: 555-274-8163
Tomas@qlmcoatingpro.example

Card 4
555-182-4407
info@qlmcoatingpro.example

Requirements
Must have
• same info as current cards with a added business
"sanitizing"

```html
<!DOCTYPE html>
<html lang="en">
<head>
<meta charset="utf-8">
<title>QLM Coating Pro – Business Card</title>
<link href="https://fonts.googleapis.com/css2?family=Lato:wght@400;700;900&display=swap" rel="stylesheet">
<style>
  :root {
    --ink: #050608;
    --ink-soft: #1b1d21;
    --paper: #ffffff;
    --brand-blue: #2f8fd8;
    --brand-blue-deep: #0d4aa6;
    --brand-blue-light: #5cb8ec;
    --text-light: #f2f4f7;
    --stage: #e9ebee;
  }
  * { margin: 0; padding: 0; box-sizing: border-box; }
  html, body { width: 1200px; height: 913px; overflow: hidden; }
  body {
    background: var(--stage);
    font-family: "Lato", Arial, sans-serif;
    position: relative;
  }
  .card {
    position: absolute;
    width: 560px;
    height: 320px;
    border-radius: 18px;
    overflow: hidden;
    box-shadow: 0 10px 30px rgba(0,0,0,.25);
  }
  .card--front { left: 40px; top: 150px; background: var(--ink); }
  .card--back {
    left: 600px; top: 460px;
    background: radial-gradient(ellipse at 60% 20%, var(--ink-soft) 0%, var(--ink) 70%);
  }
  .card__art { position: absolute; inset: 0; }

  .contact { position: absolute; left: 34px; top: 46px; color: var(--text-light); }
  .contact__name {
    font-weight: 900; font-size: 28px; color: var(--brand-blue); letter-spacing: .2px;
    white-space: nowrap;
  }
  .contact__title { font-size: 16px; margin-top: 2px; }
  .contact__rule { width: 36px; height: 3px; background: var(--brand-blue); margin: 20px 0 18px; }
  .contact__address { font-size: 15px; line-height: 20px; margin-bottom: 8px; }
  .contact__list { list-style: none; font-size: 15px; line-height: 23px; }
  .contact__list li { display: flex; align-items: center; gap: 10px; white-space: nowrap; }
  .contact__list svg { width: 14px; height: 14px; flex: none; }

  .brand {
    display: flex; align-items: center; gap: 9px;
    font-weight: 900; color: var(--brand-blue-deep); white-space: nowrap;
  }
  .brand__mark { width: 13px; height: 13px; background: var(--brand-blue-deep); flex: none; }
  .card--front .brand { position: absolute; right: 30px; top: 92px; font-size: 23px; }

  .card--back .brand {
    position: absolute; left: 0; right: 0; top: 110px; justify-content: center;
    font-size: 40px; color: var(--text-light);
  }
  .card--back .brand__mark { width: 20px; height: 20px; background: var(--brand-blue); }
  .services {
    position: absolute; left: 0; right: 0; bottom: 22px; height: 34px;
    background: linear-gradient(90deg, var(--brand-blue-deep), var(--brand-blue));
    color: var(--text-light);
    display: flex; align-items: center; justify-content: center;
    font-size: 12.5px; letter-spacing: .6px; gap: 8px;
    white-space: nowrap; padding: 0 16px;
  }
  .services__sep { opacity: .85; }
</style>
</head>
<body>

<section class="card card--front" aria-label="Business card front">
  <svg class="card__art" viewBox="0 0 560 320" preserveAspectRatio="none" aria-hidden="true">
    <path d="M245 0 C300 0 312 100 332 190 C352 270 405 320 485 320 L560 320 L560 0 Z" fill="var(--paper)"/>
    <path d="M228 0 C285 0 296 100 316 190 C336 272 385 320 465 320" fill="none" stroke="var(--brand-blue)" stroke-width="5"/>
    <path d="M258 2 C312 8 324 100 344 185 C366 268 420 314 540 318" fill="none" stroke="var(--brand-blue-light)" stroke-width="2"/>
  </svg>

  <div class="contact">
    <p class="contact__name">Gordon Thibeaux</p>
    <p class="contact__title">Precident &amp; CEO</p>
    <div class="contact__rule"></div>
    <p class="contact__address">742 Alder Ridge Rd.<br>Suite 5 Millbrook, TX 75990</p>
    <ul class="contact__list">
      <li>
        <svg viewBox="0 0 16 16"><path d="M3 1h3l1.5 4-2 1.2a9 9 0 0 0 4.3 4.3L11 8.5l4 1.5v3a2 2 0 0 1-2 2A12 12 0 0 1 1 3a2 2 0 0 1 2-2z" fill="var(--brand-blue)"/></svg>
        555-182-4407
      </li>
      <li>
        <svg viewBox="0 0 16 16"><rect x="1" y="3" width="14" height="10" rx="1" fill="var(--brand-blue)"/><path d="M1.5 3.5 8 9l6.5-5.5" fill="none" stroke="var(--ink)" stroke-width="1.3"/></svg>
        info@qlmcoatingpro.example
      </li>
      <li>
        <svg viewBox="0 0 16 16"><circle cx="8" cy="8" r="6.5" fill="none" stroke="var(--brand-blue)" stroke-width="1.3"/><path d="M1.5 8h13M8 1.5c-3 3.5-3 9.5 0 13M8 1.5c3 3.5 3 9.5 0 13" fill="none" stroke="var(--brand-blue)" stroke-width="1"/></svg>
        www.qlmcoatingpro.example
      </li>
      <li>
        <svg viewBox="0 0 16 16"><circle cx="8" cy="8" r="6.5" fill="none" stroke="var(--brand-blue)" stroke-width="1.3"/><circle cx="8" cy="8" r="1.6" fill="var(--brand-blue)"/></svg>
        qlmcoatingpro
      </li>
    </ul>
  </div>

  <div class="brand"><span class="brand__mark"></span>QLM Coating Pro</div>
</section>

<section class="card card--back" aria-label="Business card back">
  <div class="brand"><span class="brand__mark"></span>QLM Coating Pro</div>
  <div class="services">
    <span>SPRAY FOAM</span><span class="services__sep">|</span>
    <span>FIBERGLASS</span><span class="services__sep">|</span>
    <span>INSULATION</span><span class="services__sep">|</span>
    <span>ROOFING</span><span class="services__sep">|</span>
    <span>SANITIZING</span>
  </div>
</section>

</body>
</html>
```